Velmuts release concert (part 2)

Velmuts is a Reggae/Ska band from Oslo , we are releasing our first album called “overgrown” , friday 29th august at a pub called Tarnwells http://www.tarnwells.no
door open starts 21:00
Concert: 22:00
Price : 150kr

i need this to be printed in a3

Great work , could you guys insert the address and phone of the venue : Tarnwells Nedre Kvistveien 4 0462 Oslo Tlf. 937 82 214 Thanks !

```html
<!DOCTYPE html>
<html lang="en">
<head>
<meta charset="utf-8">
<title>Velmuts – Overgrown release concert</title>
<link href="https://fonts.googleapis.com/css2?family=Open+Sans:wght@300;400;600;700&family=Great+Vibes&display=swap" rel="stylesheet">
<style>
  :root {
    --salmon: #ec8176;
    --salmon-deep: #d9685d;
    --ink: #0b0b0b;
    --paper: #ffffff;
    --photo-light: #8c8c8c;
    --photo-dark: #2f2f2f;
  }
  * { margin: 0; padding: 0; box-sizing: border-box; }
  html, body { width: 849px; height: 1200px; overflow: hidden; background: var(--salmon); }
  .poster {
    position: relative;
    width: 849px;
    height: 1200px;
    background: var(--salmon);
    font-family: "Open Sans", Arial, sans-serif;
    overflow: hidden;
  }
  .band-photo {
    position: absolute;
    left: 0; top: 0;
    width: 849px; height: 440px;
    background: linear-gradient(180deg, var(--salmon) 0%, var(--salmon) 12%, var(--photo-light) 45%, var(--photo-dark) 100%);
  }
  .info-band {
    position: absolute;
    left: 0; top: 630px;
    width: 849px; height: 435px;
    background: var(--ink);
  }
  .name-badge {
    position: absolute;
    left: 200px; top: 388px;
    width: 450px; height: 168px;
  }
  .band-name {
    position: absolute;
    left: 200px; top: 425px;
    width: 450px;
    text-align: center;
    font-weight: 700;
    font-size: 60px;
    line-height: 80px;
    letter-spacing: 2px;
    color: var(--ink);
    text-transform: uppercase;
  }
  .album-title {
    position: absolute;
    left: 0; top: 545px;
    width: 849px;
    text-align: center;
    font-family: "Great Vibes", cursive;
    font-weight: 400;
    font-size: 150px;
    line-height: 1;
    color: var(--paper);
    -webkit-text-stroke: 3px var(--salmon-deep);
    paint-order: stroke fill;
    text-shadow: 6px 8px 10px rgba(0,0,0,0.45);
  }
  .release-note {
    position: absolute;
    left: 0; top: 736px;
    width: 849px;
    text-align: center;
    color: var(--paper);
    font-weight: 600;
    font-size: 27px;
    line-height: 41px;
  }
  .date {
    position: absolute;
    left: 0; top: 834px;
    width: 849px;
    text-align: center;
    color: var(--salmon);
    font-size: 38px;
    line-height: 50px;
    font-weight: 300;
  }
  .date strong { font-weight: 700; }
  .date sup { font-size: 20px; vertical-align: 15px; }
  .at {
    position: absolute;
    left: 0; top: 893px;
    width: 849px;
    text-align: center;
    color: var(--paper);
    font-size: 26px;
    line-height: 34px;
  }
  .venue-name {
    position: absolute;
    left: 0; top: 936px;
    width: 849px;
    text-align: center;
    color: var(--paper);
    font-weight: 700;
    font-size: 42px;
    line-height: 52px;
    letter-spacing: 1px;
  }
  .venue-tagline {
    position: absolute;
    left: 0; top: 988px;
    width: 849px;
    text-align: center;
    color: var(--paper);
    font-weight: 700;
    font-size: 14px;
    line-height: 18px;
    letter-spacing: 1px;
  }
  .venue-web {
    position: absolute;
    left: 0; top: 1012px;
    width: 849px;
    text-align: center;
    color: var(--paper);
    font-size: 15px;
    line-height: 20px;
    letter-spacing: 4px;
  }
  .venue-address {
    position: absolute;
    left: 0; top: 1036px;
    width: 849px;
    text-align: center;
    color: var(--paper);
    font-size: 14px;
    line-height: 20px;
    letter-spacing: 1px;
  }
  .event-details {
    position: absolute;
    left: 0; top: 1088px;
    width: 849px;
    text-align: center;
    color: var(--ink);
    font-size: 22px;
    line-height: 30.5px;
    text-transform: uppercase;
  }
</style>
</head>
<body>
  <main class="poster">
    <div class="band-photo" role="img" aria-label="Black and white photo of the eight band members standing on wide stone steps"></div>
    <div class="info-band"></div>

    <svg class="name-badge" viewBox="0 0 450 168" aria-hidden="true">
      <rect x="4" y="4" width="442" height="160" rx="60" fill="var(--paper)"/>
      <rect x="16" y="16" width="418" height="136" rx="50" fill="none" stroke="var(--salmon)" stroke-width="3" stroke-dasharray="1 7" stroke-linecap="round"/>
    </svg>
    <h1 class="band-name">Velmuts</h1>

    <h2 class="album-title">Overgrown</h2>

    <p class="release-note">FIRST ALBUM<br>LIVE PERFORMANCE</p>
    <p class="date">FRIDAY <strong>29<sup>TH</sup> AUGUST</strong></p>
    <p class="at">at</p>

    <p class="venue-name">TARNWELLS</p>
    <p class="venue-tagline">ROOTS &amp; BLUES JOINT</p>
    <p class="venue-web">WWW.TARNWELLS.NO</p>
    <p class="venue-address">Nedre Kvistveien 4, 0462 Oslo · Tlf. 937 82 214</p>

    <p class="event-details">Door open starts 21:00<br>Concert: 22:00<br>Price : 150kr</p>
  </main>
</body>
</html>
```